Business card

We need a business card design for our company based in Auckland , New Zealand called 'Kestrel + Design Ltd'. We provide architectural services. We would like to see designs that use the max. three colours (such as white, black, grey) The final design should communicate financial safety and growth."
Also I will provide our company logo. I would like to the logo to be embeded onto our business card.

Target Market(s)

new residential house, alteration & addition & light commericila design & drafting service

Industry/Entity Type

Architecture

Contact Information for Business Card

Company name: kestrel + design Ltd.
Name: Mark Telford
Job title: architectural designer & Design RQC
email address: mark@kdstudio.co.nz
mobile number: 02 5319 6620
web site: www.kdstudio.co.nz

Requirements
Must have
• My project must have..
• - embeded logo (attached company logo)
• I don't have a bigger version for our company logo, but I have one old one, so you can remove the word from it)
• - insert the attached small PDGQ logo & RQC logo
• - creative, simple and clear business card.
• - Max. three colours
Nice to have
• - Here are the samples I would like to share with you: http://www.velmorindex.com/blog/minimalistic-business-card-designs/
• I would like to have my business card like one of the creation.
Should not have
• TBA

```html
<!DOCTYPE html>
<html lang="en">
<head>
<meta charset="utf-8">
<title>Kestrel + Design Ltd — Business Card</title>
<link href="https://fonts.googleapis.com/css2?family=Open+Sans:wght@400;700&display=swap" rel="stylesheet">
<style>
  :root {
    --ink: #1a1a1a;
    --paper: #f4f3f1;
    --frame: #0d0d0d;
    --grey: #6e6e6e;
    --backdrop: #d9d8d5;
  }
  * { margin: 0; padding: 0; box-sizing: border-box; }
  html, body {
    width: 1200px; height: 882px; overflow: hidden;
    background: var(--backdrop);
    font-family: "Open Sans", Arial, sans-serif;
    color: var(--ink);
  }
  .canvas { position: relative; width: 1200px; height: 882px; }
  .card {
    position: absolute; top: 277px;
    width: 540px; height: 328px;
    background: var(--paper);
    box-shadow: 0 6px 18px rgba(0,0,0,.18);
  }
  .card--info { left: 40px; }
  .card--brand { left: 620px; border: 16px solid var(--frame); }

  .info-header { position: absolute; left: 176px; top: 58px; }
  .info-header__mark {
    position: absolute; left: 262px; top: -6px;
    width: 46px; height: 46px; border: 5px solid var(--ink); border-radius: 50%;
  }
  .company-name { font-weight: 700; font-size: 24px; letter-spacing: -0.2px; }
  .job-title { font-size: 12.5px; margin-top: 2px; }

  .contact {
    position: absolute; left: 90px; top: 148px;
    display: grid; grid-template-columns: 150px auto; column-gap: 14px; row-gap: 2px;
    font-size: 16px;
  }
  .contact dt { text-align: right; }
  .contact dd { }

  .cert-badge {
    position: absolute; left: 22px; bottom: 20px;
    width: 40px; height: 40px; border-radius: 50%;
    background: var(--ink); border: 3px solid var(--paper);
    box-shadow: 0 0 0 1.5px var(--ink);
  }

  .brand-lockup {
    position: absolute; inset: 0;
    display: flex; align-items: center; justify-content: center; gap: 18px;
  }
  .brand-lockup__mark {
    width: 58px; height: 58px; border: 7px solid var(--ink); border-radius: 50%;
  }
  .brand-lockup__name { font-weight: 700; font-size: 26px; }
</style>
</head>
<body>
<main class="canvas">
  <section class="card card--info">
    <div class="info-header">
      <span class="info-header__mark" aria-hidden="true"></span>
      <p class="company-name">kestrel + design Ltd.</p>
      <p class="job-title">architectural designer &amp; Design RQC</p>
    </div>
    <dl class="contact">
      <dt>Name:</dt><dd>Mark Telford</dd>
      <dt>email address:</dt><dd>mark@kdstudio.co.nz</dd>
      <dt>mobile number:</dt><dd>02 5319 6620</dd>
      <dt>web site:</dt><dd>www.kdstudio.co.nz</dd>
    </dl>
    <span class="cert-badge" role="img" aria-label="Licensed practitioner certification badge"></span>
  </section>

  <section class="card card--brand">
    <div class="brand-lockup">
      <span class="brand-lockup__mark" aria-hidden="true"></span>
      <p class="brand-lockup__name">kestrel + design Ltd.</p>
    </div>
  </section>
</main>
</body>
</html>
```